New business card design for Pinecrest Hollow Optometry Clinic

We need a new business card design using our existing logo (uploaded). Please do not include eyes, eye exam charts or beaches, water, sand. The logo I uploaded shows our colors of green and blue, but we are open to seeing it in black OR white. We would like to see something modern and fresh. It will need to be 2 sided. On the front we will need to be able to put a doctors name, for example-Dr Marta Kellerman and Associates. We will need to be able to change the name to other doctors names when we send for printing. The back of the card should list the following: 3817 Tarrow St, Wasaga Beach (P)705-555-0148 (E) info@phoc.ca www.phoc.ca. "We are welcoming new patients" and a line for the appointment date and time. I have uploaded the back of a card to give an example

```html
<!DOCTYPE html>
<html lang="en">
<head>
<meta charset="utf-8">
<title>Pinecrest Hollow Optometry Clinic – Business Card</title>
<link rel="stylesheet" href="https://fonts.googleapis.com/css2?family=Montserrat:wght@400;500;700&display=swap">
<style>
  :root {
    --charcoal: #3a3a3a;
    --white: #ffffff;
    --paper: #ffffff;
    --field-band: #e6e6e8;
    --brand-blue: #3a55a4;
    --brand-green: #1e9b4b;
    --ink: #333333;
    --canvas: #f2f2f2;
  }
  * { box-sizing: border-box; margin: 0; padding: 0; }
  html, body {
    width: 1200px; height: 1200px; overflow: hidden;
    background: var(--canvas);
    font-family: "Montserrat", sans-serif;
  }
  .sheet {
    width: 1200px; height: 1200px;
    display: flex; flex-direction: column; align-items: center; justify-content: center;
    gap: 44px;
  }
  .card {
    width: 900px; height: 514px;
    position: relative; overflow: hidden;
    box-shadow: 0 10px 30px rgba(0,0,0,.18);
  }

  /* Front */
  .card-front {
    background: var(--charcoal);
    display: flex; align-items: center; justify-content: center;
  }
  .front-name {
    color: var(--white);
    font-weight: 700; font-size: 50px; line-height: 1.2;
    text-align: center; letter-spacing: .5px;
  }

  /* Back */
  .card-back { background: var(--paper); }
  .welcome-band {
    position: absolute; left: 0; top: 0; width: 100%; height: 84px;
    background: var(--charcoal);
    display: flex; align-items: center; justify-content: flex-end;
    padding-right: 48px;
  }
  .welcome-text {
    color: var(--white); font-weight: 700; font-size: 40px; letter-spacing: .5px;
  }
  .clinic-name {
    position: absolute; left: 46px; top: 118px; width: 360px;
    color: var(--brand-blue); font-weight: 700; font-size: 34px; line-height: 1.15;
  }
  .contact-list {
    position: absolute; left: 470px; top: 112px;
    list-style: none;
  }
  .contact-item {
    display: flex; align-items: flex-start; gap: 14px;
    margin-bottom: 10px; font-size: 24px; line-height: 1.2;
  }
  .contact-icon { flex: 0 0 30px; width: 30px; height: 30px; margin-top: 1px; }
  .contact-address { color: var(--ink); font-weight: 500; }
  .contact-phone { color: var(--brand-green); font-weight: 700; font-size: 30px; }
  .contact-email, .contact-web { color: var(--brand-green); font-weight: 400; }

  .appointment-band {
    position: absolute; left: 0; bottom: 0; width: 100%; height: 150px;
    background: var(--field-band);
    padding: 26px 46px 0;
    color: var(--brand-blue);
  }
  .field-row { display: flex; align-items: flex-end; gap: 12px; margin-bottom: 26px; }
  .field-label { font-size: 24px; font-weight: 400; white-space: nowrap; }
  .field-label.strong { font-weight: 700; }
  .field-line { flex: 1; border-bottom: 2px solid var(--brand-blue); height: 0; margin-bottom: 6px; }
  .doctor-row { position: absolute; left: 46px; top: -10px; width: 380px; }
  .doctor-row .field-label { font-size: 22px; }
</style>
</head>
<body>
<main class="sheet">

  <section class="card card-front" aria-label="Card front">
    <p class="front-name">Pinecrest Hollow<br>Optometry Clinic</p>
  </section>

  <section class="card card-back" aria-label="Card back">
    <header class="welcome-band">
      <h2 class="welcome-text">We are Welcoming New Patients</h2>
    </header>

    <p class="clinic-name">Pinecrest Hollow<br>Optometry Clinic</p>

    <ul class="contact-list">
      <li class="contact-item">
        <svg class="contact-icon" viewBox="0 0 30 30" aria-hidden="true">
          <circle cx="15" cy="15" r="13.5" fill="none" stroke="#333" stroke-width="1.6"/>
          <path d="M15 7a5 5 0 0 0-5 5c0 4 5 10 5 10s5-6 5-10a5 5 0 0 0-5-5z" fill="#333"/>
          <circle cx="15" cy="12" r="1.8" fill="#fff"/>
        </svg>
        <span class="contact-address">3817 Tarrow St,<br>Wasaga Beach</span>
      </li>
      <li class="contact-item">
        <svg class="contact-icon" viewBox="0 0 30 30" aria-hidden="true">
          <circle cx="15" cy="15" r="13.5" fill="none" stroke="#333" stroke-width="1.6"/>
          <path d="M10 8l3 0 1.5 4-2 1.5a8 8 0 0 0 4 4l1.5-2 4 1.5 0 3c-7 1-13-5-12-12z" fill="#333"/>
        </svg>
        <span class="contact-phone">705-555-0148</span>
      </li>
      <li class="contact-item">
        <svg class="contact-icon" viewBox="0 0 30 30" aria-hidden="true">
          <circle cx="15" cy="15" r="13.5" fill="none" stroke="#333" stroke-width="1.6"/>
          <rect x="8" y="10" width="14" height="10" fill="#333"/>
          <path d="M8 10l7 6 7-6" fill="none" stroke="#fff" stroke-width="1.3"/>
        </svg>
        <span class="contact-email">info@phoc.ca</span>
      </li>
      <li class="contact-item">
        <svg class="contact-icon" viewBox="0 0 30 30" aria-hidden="true">
          <circle cx="15" cy="15" r="13.5" fill="none" stroke="#333" stroke-width="1.6"/>
          <circle cx="15" cy="15" r="7.5" fill="none" stroke="#333" stroke-width="1.3"/>
          <ellipse cx="15" cy="15" rx="3.2" ry="7.5" fill="none" stroke="#333" stroke-width="1.2"/>
          <path d="M7.5 15h15M9 11h12M9 19h12" stroke="#333" stroke-width="1.1"/>
        </svg>
        <span class="contact-web">www.phoc.ca</span>
      </li>
    </ul>

    <div class="appointment-band">
      <div class="field-row">
        <span class="field-label strong">Doctor :</span>
        <span class="field-line"></span>
      </div>
      <div class="field-row">
        <span class="field-label">Date :</span>
        <span class="field-line"></span>
        <span class="field-label">Time :</span>
        <span class="field-line"></span>
      </div>
    </div>
  </section>

</main>
</body>
</html>
```